Flyer-Design für Seniorenbetreuung
Zielgruppe
Wir sind eine Genossenschaft, welche ihren Immobilienbestand gern erweitern möchte. Dafür soll für unsere Partnerfirma (welche im Seniorenbetreuungssektor tätig ist) eine Flyer erdacht werden, welcher Senioren bzw. ihre Angehörigen anspricht die Wohneigentum besitzen. Viele Senioren besitzen Ein-, Mehrfamilienhäuser oder Eigentumswohnungen und können oder wollen diese nicht weiter vererben. Zusätzlich sind sie durch die Kosten des Eigentums, wie Steuern oder Instandhaltungskosten belastet. Unsere Genossenschaft bietet eine Lösung des Problems. Eine Übernahme des Eigentums bei gleichzeitigem lebenslangem Wohnrecht. Die Zielgruppe soll in dem Flyer auf die bestehende Probleme angesprochen werden und gleichzeitig eine individuelle Lösung angeboten werden, welche eine Mitgliedschaft in dem sozialen Verbund der Genossenschaft ist.
Aufgabenstellung
Der Designer hat hier völlig freie Hand. Es sollte auf die Zielgruppe passen.
Passende Texte soll sich der Designer selbst erdenken.
Nachtrag: Ich habe mittlerweile viele Zuschriften bekommen, dass die Aufgabenstellung sich Texte auszudenken etwas zu allgemein gefasst ist, daher versuche ich hier nochmal etwas Licht in Dunkle zu bringen. Ich habe genauso wenig eine Idee, wie und mit welcher Wortwahl ein Senior auf einfühlsame Weise darauf angesprochen werden soll, ob er nicht sein Haus verkaufen möchte. Meine bisherigen Ideen waren:
'Haben sie schon einmal über den Verkauf ihrer Immobilie nachgedacht? Wussten sie, dass sie ihr Wohneigentum im vollen Umfang weiter nutzen können, ohne weiter die Kosten tragen zu müssen? Sie wollen wissen wie? Rufen sie doch einfach an und ich werde ihnen genau erklären, welche Vorzüge die Mitgliedschaft in einer Genossenschaft mit sich bringt.'
Allerdings erscheint mir das viel zu direkt und ich finde nicht die richtigen Worte diese Personengruppe in dem Maße anzusprechen, wie es nötig wäre, um sie zu einem Anruf zu bewegen. Daher hatte ich gehofft, dass sie hier ein findiger Designer findet, welcher eine bessere kreative Art hat als ich.
Vielleicht ist es die falsche Plattform, vielleicht schaffen wir es nicht die Vorgaben zu spezifizieren. Bilder anzuordnen ist sicher sehr wichtig, auch ist es wichtig aufhellende Elemente einzubringen. Aber wir suchen jemanden der einen Flyer so gestalten kann das der Flyer etwas ausdrückt, das eine Botschaft vermittelt wird, das auf einem Blick der Senior den Wunsch verspürt, bei uns anzurufen. Das heißt viel wichtiger als Bilder, ist der Inhalt der Ansprache. Nicht unbedingt der Inhalt, sondern das WIE. Nochmal: wir wollen ältere Menschen dazu bewegen ihr Eigentum auf Grund von Reperaturrückstau, Überlastung, gesundheitlichen Einschränkungen, finanziellen Schwierigkeiten, zu großem Aufwand in eine Genossenschaft einzubringen. Ds heißt S..

```html
<!DOCTYPE html>
<html lang="de">
<head>
<meta charset="utf-8">
<title>Flyer – Stressfreie Immobilienverwaltung</title>
<link href="https://fonts.googleapis.com/css2?family=Gelasio:wght@400&family=Open+Sans:ital,wght@0,400;0,700;1,700&display=swap" rel="stylesheet">
<style>
  :root {
    --paper: #efefef;
    --ink: #111111;
    --accent: #c67c62;
    --band: #e8c9bf;
    --white: #ffffff;
  }
  * { margin: 0; padding: 0; box-sizing: border-box; }
  html, body { width: 1200px; height: 3395px; overflow: hidden; }
  body {
    background: var(--paper);
    font-family: "Open Sans", Arial, sans-serif;
    color: var(--ink);
    position: relative;
  }
  .headline {
    position: absolute;
    left: 93px;
    top: 112px;
    font-family: "Gelasio", Georgia, serif;
    font-weight: 400;
    font-size: 134px;
    line-height: 138px;
    letter-spacing: -1px;
    white-space: nowrap;
  }
  .headline .accent { color: var(--accent); }
  .hero-photo {
    position: absolute;
    left: 0; top: 731px;
    width: 1200px; height: 740px;
    display: block;
  }
  .content {
    position: absolute;
    left: 93px;
    width: 1080px;
  }
  .content h2 {
    font-weight: 700;
    font-size: 53px;
    line-height: 68px;
    color: var(--accent);
    margin-bottom: 12px;
    white-space: nowrap;
  }
  .content p {
    font-size: 42px;
    line-height: 53px;
    margin-bottom: 22px;
    white-space: nowrap;
  }
  .offer { top: 1540px; }
  .support { top: 2215px; }
  .contact-band {
    position: absolute;
    left: 0; top: 2815px;
    width: 1200px; height: 580px;
    background: var(--band);
  }
  .contact-band h3 {
    position: absolute;
    left: 93px; top: 50px;
    font-style: italic;
    font-weight: 700;
    font-size: 53px;
    line-height: 68px;
    white-space: nowrap;
  }
  .address {
    position: absolute;
    left: 93px; top: 200px;
    font-size: 44px;
    line-height: 62px;
    font-style: normal;
    white-space: nowrap;
  }
  .company-name-box {
    position: absolute;
    left: 716px; top: 233px;
    width: 484px; height: 165px;
    background: var(--white);
    display: flex; align-items: center; justify-content: center;
    font-size: 34px;
    letter-spacing: 1px;
  }
  .web-line {
    position: absolute;
    left: 93px; top: 430px;
    font-size: 36px;
    line-height: 50px;
    white-space: nowrap;
  }
</style>
</head>
<body>
  <h1 class="headline">Die <span class="accent">stressfreie</span><br>Verwaltung all<br>Ihrer Immobilien<br>übernehmen wir.</h1>

  <svg class="hero-photo" role="img" aria-label="Foto: zwei Seniorenfiguren auf einer Bank, ein kleines Modellhaus mit orangem Dach und ein Stapel Münzen" viewBox="0 0 1200 740" preserveAspectRatio="none">
    <defs>
      <linearGradient id="heroTone" x1="0" y1="0" x2="0" y2="1">
        <stop offset="0" stop-color="#e6e6e6"/>
        <stop offset="0.55" stop-color="#dcdad8"/>
        <stop offset="1" stop-color="#f2f2f2"/>
      </linearGradient>
    </defs>
    <rect width="1200" height="740" fill="url(#heroTone)"/>
  </svg>

  <section class="content offer">
    <h2>Wir bieten Ihnen solide Lösungen für<br>alle Ihre Häuser oder Wohnungen.</h2>
    <p>Ihre Immobilien sind neben der Rente Ihre einzige<br>Einnahmequelle? Aber das finanzielle Polster<br>wird plötzlich immer kleiner und die Ausgaben<br>für Reparaturen und Verwaltungsgesellschaften<br>werden immer höher?</p>
    <p>Vielleicht sind Sie selbst nicht mehr in der Lage die<br>organisatorischen Dinge mit Mietern und Behörden<br>zu regeln?</p>
  </section>

  <section class="content support">
    <h2>Die Genossenschaft xy unterstützt Sie<br>auch bei bewohnten Immobilien, die<br>Sie vermieten.</h2>
    <p>Ihre Einkünfte aus Vermietung bleiben Ihnen<br>erhalten und die Zeiten von teuren Hausverwaltern<br>und Sorgen um die Ausgaben sind endlich vorbei.</p>
    <p>Für mehr Entspannung, Ruhe und Freude in Ihrer<br>schönsten Zeit des Lebens.</p>
  </section>

  <footer class="contact-band">
    <h3>Wir beraten Sie am Telefon oder mit<br>Terminvereinbarung bei Ihnen zuhause.</h3>
    <address class="address">Genossenschaft xy<br>Straße 1 | 13332 xxxxxx<br>Telefon 0151 xxxxxxxx</address>
    <div class="company-name-box">FIRMENLOGO</div>
    <p class="web-line">wohnverbund-elbtal.de | kontakt@wohnverbund-elbtal.de</p>
  </footer>
</body>
</html>
```